Plakat für Hersteller von Maultaschen und Knödeln
Zielgruppe
Mit meiner Manufaktur Rinnfalten & Co stelle ich Maultaschen und Knödel her. Produziert wird mit hochwertigen, möglichst regionalen Zutaten und mit dem Anspruch, traditionelle Klassiker in zeitgemäßer Qualität anzubieten.
Im Mittelpunkt stehen Frische, Transparenz und ehrliches Handwerk. Die Produkte werden mit Sorgfalt hergestellt und sind für den direkten Verkauf auf dem Brunnwaldener Wochenmarkt bestimmt. Rinnfalten & Co verbindet bodenständige Küche mit regionaler Identität – unkompliziert, authentisch und genussorientiert.
Zielgruppe rund um den Brunnwaldener Wochenmarkt:
- Marktbesucher mit Qualitätsbewusstsein, die gezielt regionale und handwerklich hergestellte Lebensmittel kaufen
- Berufstätige und Familien, die hochwertige, frisch produzierte Gerichte für zu Hause suchen
- Genussorientierte Kundinnen und Kunden, die traditionelle Küche schätzen
- Seniorinnen und Senioren, die klassische Hausmannskost bevorzugen
- Regionalverbundenen Verbraucherinnen und Verbrauchern, die lokale Anbieter unterstützen möchten
Der Brunnwaldener Wochenmarkt zieht ein vielfältiges Publikum an, das Wert auf persönliche Beratung, Frische und nachvollziehbare Herkunft legt. Rinnfalten positioniert sich hier als authentischer, spezialisierter Anbieter für handgemachte Teigklassiker mit klarem kulinarischem Profil.
Aufgabenstellung
Das Plakat soll in A5, A4, A3 und A2 nutzbar sein und der Text soll austauschbar sein.
Das Plakat soll gut zum Wochenmarkt passen und ehrliches, qualitativ hochwertiges Handwerk ausdrücken und vor allem Lust auf Maultaschen und Knödel machen. Es soll zu meinen Marktstand (Monza Rot) und dem Logo passen. Das Logo soll sehr präsent sein.

```html
<!DOCTYPE html>
<html lang="de">
<head>
<meta charset="utf-8">
<title>Rinnfalten &amp; Co – Plakat</title>
<link href="https://fonts.googleapis.com/css2?family=Bebas+Neue&family=Lobster&family=Lato:wght@300;400;700&display=swap" rel="stylesheet">
<style>
  :root {
    --monza-red: #a8141c;
    --monza-red-deep: #8a0f16;
    --cream-gold: #ecdcaa;
    --ribbon-cream: #f6f2e8;
    --ribbon-gold: #b68a4c;
    --ink: #1b1b1b;
    --ink-soft: #444444;
    --paper: #ffffff;
    --leaf-green: #8fb82a;
    --soft-pink: #f3c9c9;
  }
  * { margin: 0; padding: 0; box-sizing: border-box; }
  html, body { width: 800px; height: 1200px; overflow: hidden; background: var(--paper); }
  .poster {
    position: relative;
    width: 800px;
    height: 1200px;
    overflow: hidden;
    background: var(--paper);
    font-family: "Lato", sans-serif;
  }
  .red-field {
    position: absolute;
    left: 0; top: 0;
    width: 800px; height: 1020px;
  }
  .brand {
    position: absolute;
    top: 64px; left: 0; width: 800px;
    display: flex; justify-content: center; align-items: center; gap: 12px;
  }
  .brand-dot {
    width: 22px; height: 22px; border-radius: 50%;
    background: var(--leaf-green);
  }
  .brand-name {
    font-family: "Lato", sans-serif;
    font-weight: 400;
    font-size: 38px;
    color: var(--monza-red);
    letter-spacing: 0.5px;
  }
  .headline {
    position: absolute;
    top: 200px; left: 0; width: 800px;
    text-align: center;
    font-family: "Bebas Neue", sans-serif;
    font-size: 74px;
    letter-spacing: 1px;
    word-spacing: 8px;
    color: var(--cream-gold);
    line-height: 1;
  }
  .subline {
    position: absolute;
    top: 274px; left: 0; width: 800px;
    text-align: center;
    font-family: "Lobster", cursive;
    font-size: 40px;
    color: var(--paper);
    line-height: 1.1;
  }
  .photo-row {
    position: absolute;
    top: 345px; left: 35px;
    display: flex; gap: 15px;
  }
  .photo {
    width: 235px; height: 231px;
    border: 2px solid #f4f1ea;
  }
  .photo--ingredients { background: linear-gradient(135deg, #b87a3e 0%, #d9a86a 45%, #3f6b2a 80%, #7a3b3b 100%); }
  .photo--handwork { background: linear-gradient(160deg, #d8d2c8 0%, #bfae96 45%, #e6dccb 75%, #c9a982 100%); }
  .photo--dish { background: linear-gradient(135deg, #2a1d17 0%, #e2bc62 45%, #c08a3c 65%, #3a2a20 100%); }
  .ribbon {
    position: absolute;
    top: 612px; left: 50px;
    width: 700px; height: 190px;
  }
  .ribbon-text {
    position: absolute;
    top: 643px; left: 0; width: 800px;
    text-align: center;
    font-family: "Lobster", cursive;
    font-size: 26px;
    line-height: 35px;
    color: var(--ink);
  }
  .benefits {
    position: absolute;
    top: 748px; left: 0; width: 800px;
    list-style: none;
    text-align: center;
  }
  .benefit { margin-bottom: 8px; }
  .benefit-title {
    display: inline-flex; align-items: center; gap: 14px;
    font-family: "Lobster", cursive;
    font-size: 26px;
    color: var(--cream-gold);
    line-height: 37px;
  }
  .benefit-title::before {
    content: "";
    width: 9px; height: 9px; border-radius: 50%;
    background: var(--cream-gold);
    box-shadow: 0 0 0 3px var(--monza-red), 0 0 0 5px var(--cream-gold);
  }
  .benefit-text {
    font-weight: 300;
    font-size: 20px;
    color: var(--soft-pink);
    line-height: 34px;
  }
  .footer {
    position: absolute;
    top: 1054px; left: 0; width: 800px;
    text-align: center;
  }
  .footer-call {
    font-weight: 700;
    font-size: 28px;
    line-height: 40px;
    color: var(--ink);
  }
  .footer-tagline {
    margin-top: 8px;
    font-weight: 300;
    font-size: 18px;
    color: var(--ink-soft);
  }
</style>
</head>
<body>
<main class="poster">
  <svg class="red-field" viewBox="0 0 800 1020" aria-hidden="true">
    <defs>
      <radialGradient id="redGlow" cx="50%" cy="45%" r="65%">
        <stop offset="0" stop-color="#b3161f"/>
        <stop offset="1" stop-color="#8a0f16"/>
      </radialGradient>
    </defs>
    <path d="M0 92 Q400 250 800 92 L800 1020 L0 1020 Z" fill="url(#redGlow)"/>
  </svg>

  <header class="brand">
    <span class="brand-dot"></span>
    <span class="brand-name">Rinnfalten &amp; Co</span>
  </header>

  <h1 class="headline">Echt. Handgemacht. Lecker.</h1>
  <p class="subline">Maultaschen &amp; Knödel wie hausgemacht.</p>

  <section class="photo-row">
    <div class="photo photo--ingredients" role="img" aria-label="Foto: frische Zutaten – Eier, Mehl, Hackfleisch und Petersilie auf Holzbrett"></div>
    <div class="photo photo--handwork" role="img" aria-label="Foto: Hände bestäuben frisch geformte Maultaschen mit Mehl"></div>
    <div class="photo photo--dish" role="img" aria-label="Foto: angebratene Maultaschen mit Zwiebeln und Petersilie auf dunklem Teller"></div>
  </section>

  <svg class="ribbon" viewBox="0 0 700 190" aria-hidden="true">
    <path d="M0 100 L100 70 L110 150 L20 175 L45 135 Z" fill="var(--ribbon-cream)" stroke="var(--ribbon-gold)" stroke-width="4"/>
    <path d="M700 100 L600 70 L590 150 L680 175 L655 135 Z" fill="var(--ribbon-cream)" stroke="var(--ribbon-gold)" stroke-width="4"/>
    <path d="M100 130 L145 120 L110 150 Z" fill="var(--ribbon-gold)"/>
    <path d="M600 130 L555 120 L590 150 Z" fill="var(--ribbon-gold)"/>
    <path d="M65 45 Q350 -5 640 45 L625 130 Q350 90 75 130 Z" fill="var(--ribbon-cream)" stroke="var(--ribbon-gold)" stroke-width="5"/>
  </svg>
  <p class="ribbon-text">Bei Rinnfalten &amp; Co verbinden wir<br>bodenständiger Küche mit regionaler Identität</p>

  <ul class="benefits">
    <li class="benefit">
      <span class="benefit-title">Frische aus der Region:</span>
      <p class="benefit-text">Hochwertige Zutaten, ehrliches Handwerk.</p>
    </li>
    <li class="benefit">
      <span class="benefit-title">Tradition trifft Moderne:</span>
      <p class="benefit-text">Klassische Rezepte in zeitgemäßer Qualität.</p>
    </li>
    <li class="benefit">
      <span class="benefit-title">Direkt vom Erzeuger:</span>
      <p class="benefit-text">Mit Liebe in unserer Manufaktur hergestellt.</p>
    </li>
  </ul>

  <footer class="footer">
    <p class="footer-call">Besuchen Sie uns an unserem Stand (Karmin-Rot)<br>auf dem Brunnwaldener Wochenmarkt!</p>
    <p class="footer-tagline">Rinnfalten &amp; Co – Weil Qualität man schmeckt.</p>
  </footer>
</main>
</body>
</html>
```